Ned Walcott Fairway Lessons Rack Card

The flyer will be a rack card. Front side only. Nothing on back. 3.75 inches by 8.5 inches. Or close to that. I’d like it to be as colorful as possible and to include several logos in different places.
The brochure is to attract golfers attention and still look traditional and classy not crazy or to artsy. Golf is a very traditional sport and would just like it to look professional and welcoming so golfers no I’m credible in my teaching and they will learn something. I will send a rough idea and a sample of one I had before but use your creative skills and ingenuity to design it. You will have to put my name: Ned Walcott under the TLQ logo. It is a requirement by the TLQ. Also the logo size must me .0875 inches high. If possible use a gotham or Hoefler text type or something businesslike or similar for my name. Also I am sorry for the different logos available on this file because I am not tech savvy so you will have to choose the best logo and cut it out of the grouping to match what you want to do. I am sorry for all the details. I will be available all weekend if you need more info. or help. I am sure you are very skilled and can tell I am not. Sorry. I laid out a sketch for you so you know what info. verbiage is important. and where to somewhat place the logos. Up to your skill for most of it. Your design! Go for it.!

Target Market(s)

Golfers of all ages from 18-70. Men and Women.

Industry/Entity Type

Golf Industry. Teaching and learning game if golf

Font styles to use
Sans Serif
Other font styles liked:
• Mixture maybe traditional type. Easy to read.

Colors

Designer to choose only greyscale colors for use in the design.

Requirements
Must have
• My Ned Walcott golf logo and the TLQ official logo. Also will send several other logos to put in. I will tell you where they should go on the rack card.
Nice to have
• Maybe a golf picture from a course with a green and flag as the one on my old brochure I’m sending or similar. It just adds color and eye catching
Should not have
• Nothing hard to read or difficult to comprehend. Pretty straight forward and quality and style in a traditional sense,

```html
<!DOCTYPE html>
<html lang="en">
<head>
<meta charset="utf-8">
<title>Ned Walcott Fairway Lessons – Rack Card</title>
<link rel="stylesheet" href="https://fonts.googleapis.com/css2?family=Montserrat:wght@500;600;700;800&display=swap">
<style>
  :root {
    --page: #ececec;
    --card: #ebebeb;
    --ink: #141414;
    --black: #151515;
    --white: #ffffff;
    --grey-dark: #666666;
    --grey-mid: #8c8c8c;
    --grey-light: #a9a9a9;
    --grey-soft: #b9b9b9;
    --photo-top: #dcdcdc;
    --photo-bottom: #6f6f6f;
  }
  * { box-sizing: border-box; margin: 0; padding: 0; }
  html, body { width: 738px; height: 1200px; overflow: hidden; }
  body { background: var(--page); font-family: "Montserrat", Arial, sans-serif; color: var(--ink); position: relative; }

  .rack-card { position: absolute; left: 109px; top: 10px; width: 520px; height: 1180px; background: var(--card); overflow: hidden; }
  .rack-card svg.backdrop { position: absolute; left: 0; top: 0; }
  .abs { position: absolute; }

  .brand-name { left: 34px; top: 42px; font-size: 17px; font-weight: 700; color: #2a2a2a; letter-spacing: .5px; display: flex; align-items: center; gap: 7px; }
  .brand-name .dot { width: 10px; height: 10px; border-radius: 50%; background: #2a2a2a; }

  .price-badge { left: 304px; top: 277px; width: 192px; height: 192px; border-radius: 50%; background: var(--white); }
  .price-badge .inner { position: absolute; inset: 8px; border-radius: 50%; background: var(--black); color: var(--white); text-align: center; padding-top: 30px; }
  .price-badge .offer { font-size: 13px; font-weight: 600; line-height: 16px; }
  .price-badge .reg { font-size: 21px; font-weight: 600; color: #d2d2d2; margin-top: 4px; }
  .price-badge .rule { width: 142px; height: 1px; background: #7a7a7a; margin: 6px auto 6px; }
  .price-badge .hour { font-size: 13px; font-weight: 600; }
  .price-badge .sale { font-size: 23px; font-weight: 700; color: #d2d2d2; margin-top: 2px; }
  sup { font-size: .45em; vertical-align: top; position: relative; top: .1em; }

  .headline { left: 26px; top: 492px; font-size: 33px; font-weight: 800; letter-spacing: .2px; }

  .includes-tab { left: 0; width: 131px; height: 27px; border-radius: 0 14px 14px 0; font-size: 14px; font-weight: 600; padding-left: 28px; line-height: 27px; }
  .includes-tab.light { top: 549px; background: var(--grey-soft); color: #2a2a2a; }
  .includes-tab.dark { top: 920px; background: var(--grey-light); color: var(--white); padding-left: 22px; }

  .ball { display: inline-block; width: 6px; height: 6px; border-radius: 50%; background: currentColor; margin: 0 6px 2px 0; vertical-align: middle; }
  .feature-list { left: 18px; top: 590px; width: 470px; font-size: 14.6px; font-weight: 500; line-height: 22px; }
  .feature-list .indent { padding-left: 12px; }

  .partner { top: 662px; font-size: 25px; font-weight: 800; color: #2a2a2a; }
  .partner.one { left: 211px; }
  .partner.two { left: 355px; }

  .side-note { right: 20px; text-align: right; font-size: 14.6px; font-weight: 500; line-height: 21px; }
  .side-note.info { top: 706px; }
  .side-note.level { top: 759px; }

  .package-title { left: 29px; top: 740px; font-size: 20px; font-weight: 700; color: var(--grey-light); line-height: 28px; }
  .package-row { left: 18px; color: var(--white); font-size: 16px; font-weight: 500; display: flex; align-items: baseline; gap: 10px; }
  .package-row.lessons { top: 815px; }
  .package-row.deal { top: 852px; }
  .package-row .reg { font-size: 24px; font-weight: 700; color: var(--grey-light); margin-left: 4px; }
  .package-row .now { font-size: 24px; font-weight: 700; color: #d0d0d0; }
  .package-rule { left: 29px; top: 895px; width: 317px; height: 1px; background: #cfcfcf; }

  .lesson-list { left: 18px; top: 964px; color: var(--white); font-size: 15px; font-weight: 500; line-height: 21px; }
  .lesson-list .indent { padding-left: 18px; }

  .seal { left: 419px; width: 80px; height: 80px; border-radius: 50%; background: #8e8e8e; border: 4px solid #d6d6d6; box-shadow: 0 0 0 2px #6b6b6b; }
  .seal.first { top: 885px; }
  .seal.second { top: 991px; }

  .phone-pill { left: 161px; top: 1071px; width: 198px; height: 36px; border-radius: 18px; background: var(--grey-dark); color: var(--white); font-size: 20px; font-weight: 600; display: flex; align-items: center; justify-content: center; gap: 8px; }

  .contact-row { left: 0; top: 1134px; width: 520px; display: flex; justify-content: center; gap: 16px; font-size: 14px; font-weight: 600; }
  .contact-row span { display: flex; align-items: center; gap: 7px; }
</style>
</head>
<body>
<div class="rack-card">
  <svg class="backdrop" width="520" height="1180" viewBox="0 0 520 1180" aria-hidden="true">
    <defs>
      <linearGradient id="fairway" x1="0" y1="0" x2="0" y2="1">
        <stop offset="0" stop-color="var(--photo-top)"/>
        <stop offset=".55" stop-color="#9a9a9a"/>
        <stop offset="1" stop-color="var(--photo-bottom)"/>
      </linearGradient>
    </defs>
    <!-- upper grey bands -->
    <path d="M370 0 H520 V300 C470 400 360 440 220 430 C120 424 40 400 0 380 V300 C60 360 160 400 260 390 C380 375 440 250 430 120 C425 70 400 30 370 0 Z" fill="var(--grey-dark)"/>
    <path d="M0 316 C60 420 170 470 260 462 C380 452 460 380 520 290 V360 C460 440 370 480 260 482 C150 484 50 440 0 400 Z" fill="var(--grey-light)"/>
    <!-- lower black wave -->
    <path d="M0 735 C40 705 75 690 110 690 C230 690 360 820 520 873 V1180 H0 Z" fill="var(--black)"/>
    <!-- bottom bands -->
    <path d="M0 1110 C120 1085 300 1080 520 1105 V1180 H0 Z" fill="var(--grey-mid)"/>
    <path d="M0 1140 C140 1100 330 1095 520 1120 V1180 H0 Z" fill="var(--white)"/>
  </svg>

  <div class="abs" role="img" aria-label="Golf course photo: iron club beside a ball on the fairway with a flag on the green" style="left:0;top:-39px;width:424px;height:424px;border-radius:50%;background:linear-gradient(180deg,var(--photo-top) 0%,#c4c4c4 40%,#5a5a5a 52%,#9c9c9c 60%,var(--photo-bottom) 100%);"></div>

  <div class="abs brand-name"><span class="dot"></span>Ned Walcott</div>

  <div class="abs price-badge">
    <div class="inner">
      <div class="offer">One Time Limited<br>Offer</div>
      <div class="reg">REG $79<sup>00</sup></div>
      <div class="rule"></div>
      <div class="hour">(1-Hour Analysis)</div>
      <div class="sale">$59<sup>99</sup></div>
    </div>
  </div>

  <h1 class="abs headline">GOLF SWING ANALYSIS</h1>

  <div class="abs includes-tab light">INCLUDES:</div>
  <div class="abs feature-list">
    <div><span class="ball"></span>Swing Analysis w/Video &nbsp;<span class="ball"></span>Review Of Swing Technique</div>
    <div class="indent">Suggested Tips &amp; Drills &nbsp;<span class="ball"></span>Video and Summary sent to</div>
    <div class="indent">your mobile devices</div>
  </div>

  <div class="abs partner one">Trackvue</div>
  <div class="abs partner two">Motionly</div>

  <div class="abs side-note info">Additional: Info <span class="ball"></span><br>@www.NWALCOTT.COM&nbsp;&nbsp;</div>
  <div class="abs side-note level">Beginners to <span class="ball"></span><br>Advanced&nbsp;&nbsp;</div>

  <div class="abs package-title">Special lesson<br>package</div>
  <div class="abs package-row lessons"><span><span class="ball"></span>3-1 hour lessons</span><span class="reg">REG $237<sup>00</sup></span></div>
  <div class="abs package-row deal"><span class="now"><span class="ball"></span>$225<sup>00</sup></span><span>(Limited Deal)</span></div>
  <div class="abs package-rule"></div>

  <div class="abs includes-tab dark">INCLUDES:</div>
  <div class="abs lesson-list">
    <div><span class="ball"></span>&nbsp;Video analysis &nbsp;<span class="ball"></span>Lesson</div>
    <div><span class="ball"></span>&nbsp;Summary and video review sent to</div>
    <div class="indent">mobile devices &nbsp;<span class="ball"></span>Tips and drills</div>
    <div><span class="ball"></span>Action plan to improve</div>
  </div>

  <div class="abs seal first" role="img" aria-label="TLQ member badge"></div>
  <div class="abs seal second" role="img" aria-label="Satisfaction guarantee seal"></div>

  <div class="abs phone-pill">
    <svg width="18" height="18" viewBox="0 0 24 24" aria-hidden="true"><path fill="#fff" d="M6.6 10.8a15.1 15.1 0 0 0 6.6 6.6l2.2-2.2c.3-.3.7-.4 1-.2 1.1.4 2.3.6 3.6.6.6 0 1 .4 1 1V20c0 .6-.4 1-1 1A17 17 0 0 1 3 4c0-.6.4-1 1-1h3.5c.6 0 1 .4 1 1 0 1.3.2 2.5.6 3.6.1.3 0 .7-.2 1z"/></svg>
    410-555-0186
  </div>

  <div class="abs contact-row">
    <span><svg width="18" height="13" viewBox="0 0 18 13" aria-hidden="true"><rect width="18" height="13" fill="#222"/><path d="M0 0 L9 7 L18 0" stroke="#fff" stroke-width="1.5" fill="none"/></svg>nwalcott@TLQ.com</span>
    <span><svg width="16" height="16" viewBox="0 0 16 16" aria-hidden="true"><g fill="none" stroke="#222" stroke-width="1.4"><circle cx="8" cy="8" r="7"/><ellipse cx="8" cy="8" rx="3" ry="7"/><path d="M1 8h14"/></g></svg>NWALCOTTLESSONS.COM</span>
  </div>
</div>
</body>
</html>
```